Verpackungen für kleine Imkerei
Zielgruppe
Wir sind eine kleine Imkerei aus dem Aargau (Schweiz) und stellen zusammen mit unseren glücklichen Bienen feinsten Honig her. Gerne möchten wir unseren visuelle Kommunikation nach aussen mit Hilfe eines neuen Etiketts verbessern.
Aufgabenstellung
Das Etikett muss rechteckig sein und wir auf einem runden Glas aufgeklebt. Die Maximalgrösse ist 210x45mm (beim 500g Glas) und entsprechend kleiner bei kleineren Einheiten. Wir möchten ein Grunddesign, welches adaptierbar ist auf die weiteren Sorten. (Waldhonig, Blütenhonig, cremiger Blütenhonig, Zürcher Stadthonig, Badener Stadthonig, Lenzburger Stadthonig). Barcode muss keinen eingefügt werden, nur die gesetzlichen Daten müssen auf dem Etiektt stehen. Weitere Wünsche und Anmerkungen befinden sich im pdf.
Sollten Dateien oder Bilder nachgereicht werden, bitte melden!

```html
<!DOCTYPE html>
<html lang="de">
<head>
<meta charset="utf-8">
<title>Sonnwabe Blütenhonig – Etikett</title>
<link href="https://fonts.googleapis.com/css2?family=Patrick+Hand+SC&display=swap" rel="stylesheet">
<style>
  :root {
    --page-bg: #ececec;
    --label-paper: #fbfbfc;
    --band-pink: #dc7a98;
    --accent-magenta: #b8275a;
    --ink: #1c1c1c;
    --wash-pink: #f3b6cb;
    --wash-pink-light: #fbe3ec;
    --placeholder-warm: #efd9a6;
  }
  * { box-sizing: border-box; margin: 0; padding: 0; }
  html, body { width: 1200px; height: 800px; overflow: hidden; }
  body {
    background: var(--page-bg);
    font-family: "Patrick Hand SC", "Comic Sans MS", cursive;
    color: var(--ink);
    position: relative;
  }
  .label {
    position: absolute;
    left: 20px; top: 276px;
    width: 1160px; height: 248px;
    background: var(--label-paper);
    box-shadow: 0 2px 6px rgba(0,0,0,.12);
    overflow: hidden;
  }
  .label__band {
    position: absolute; left: 0; right: 0; bottom: 0;
    height: 20px; background: var(--band-pink);
  }
  .wash {
    position: absolute;
    border-radius: 50%;
    filter: blur(14px);
    background: radial-gradient(ellipse at center, var(--wash-pink) 0%, var(--wash-pink-light) 60%, transparent 100%);
  }
  .wash--left  { left: 110px; top: -30px; width: 320px; height: 170px; }
  .wash--right { right: -20px; top: -30px; width: 360px; height: 180px; }
  .wash--right-low { right: 30px; top: 120px; width: 200px; height: 120px; }
  .wash--center { left: 430px; top: 110px; width: 320px; height: 140px; }
  .flowers {
    position: absolute; left: 370px; top: 120px;
    width: 440px; height: 108px;
    border-radius: 220px 220px 0 0;
    background: radial-gradient(ellipse at 50% 100%, rgba(204,63,116,.45) 0%, rgba(243,182,203,.35) 55%, transparent 80%);
  }
  .bee-spot {
    position: absolute; width: 26px; height: 24px; border-radius: 50%;
    background: var(--placeholder-warm);
    opacity: .8;
  }
  .info, .contact {
    position: absolute; top: 40px;
    font-size: 14px; line-height: 21px;
    text-transform: uppercase;
  }
  .info { left: 24px; }
  .contact { right: 24px; text-align: right; }
  .info__heading { color: var(--accent-magenta); }
  .info__gap { margin-top: 6px; }
  .brand {
    position: absolute; left: 0; right: 0; top: 44px;
    text-align: center;
  }
  .brand__name {
    font-size: 62px; line-height: 1; font-weight: 400; color: var(--ink);
  }
  .brand__variety {
    margin-top: 30px;
    font-size: 34px; line-height: 1; color: var(--ink);
  }
  .brand__kind {
    font-size: 17px; color: #fff; letter-spacing: 1px;
    text-shadow: 0 0 2px rgba(184,39,90,.6);
  }
</style>
</head>
<body>
  <main class="label" aria-label="Etikett Sonnwabe Blütenhonig">
    <div class="wash wash--left" role="img" aria-label="Rosa Aquarellfläche"></div>
    <div class="wash wash--right" role="img" aria-label="Rosa Aquarellfläche"></div>
    <div class="wash wash--right-low" role="img" aria-label="Rosa Aquarellfläche"></div>
    <div class="wash wash--center" role="img" aria-label="Rosa Aquarellfläche"></div>
    <div class="flowers" role="img" aria-label="Gezeichnete Blumenwiese in Magenta"></div>

    <span class="bee-spot" style="left:198px;top:56px" role="img" aria-label="Illustration einer fliegenden Biene"></span>
    <span class="bee-spot" style="left:166px;top:162px" role="img" aria-label="Illustration einer fliegenden Biene"></span>
    <span class="bee-spot" style="left:1043px;top:26px" role="img" aria-label="Illustration einer fliegenden Biene"></span>
    <span class="bee-spot" style="left:1004px;top:126px" role="img" aria-label="Illustration einer fliegenden Biene"></span>

    <section class="info">
      <p class="info__heading">Schweizer Blütenhonig</p>
      <p>Honig gut verschlossen,</p>
      <p>kühl (bei max. 15°),</p>
      <p>dunkel und trocken lagern</p>
      <p class="info__heading info__gap">Mindestens haltbar bis</p>
      <p>August 2022</p>
      <p class="info__gap"><span class="info__heading">Warenlos Nr.</span> 01092018</p>
      <p class="info__gap"><span class="info__heading">Nettogewicht</span> 500g</p>
    </section>

    <section class="brand">
      <h1 class="brand__name">Sonnwabe</h1>
      <p class="brand__variety">Blüten</p>
      <p class="brand__kind">· HONIG ·</p>
    </section>

    <section class="contact">
      <p class="info__heading">Adresse</p>
      <p>Ursula und Peter Karrigo</p>
      <p>Lindenweg 4</p>
      <p>5600 Lindhofen</p>
      <p class="info__heading info__gap">Web</p>
      <p>www.sonnwabe.ch</p>
      <p class="info__heading info__gap">Mail</p>
      <p>info@sonnwabe.ch</p>
    </section>

    <div class="label__band"></div>
  </main>
</body>
</html>
```